HARBORLINE AUTO GLASS

Mobile Glass Shop:

1) Windshield REPAIR 2)Windshield replacment 3) Rear Windshield Replacment 4) Side Window Replacment 5) car window replacment 6) Power Window Repair.

Schedual a service within 24 hour with one of our certified technicians.

See "clearvane auto repair" web site for referance on the nature of our buisness and service. www.clearvane-example.com

```html
<!DOCTYPE html>
<html lang="en">
<head>
<meta charset="utf-8">
<title>Harborline Auto Glass</title>
<link rel="stylesheet" href="https://fonts.googleapis.com/css2?family=Oswald:wght@500;600;700&family=Roboto:ital,wght@0,400;0,500;1,400&display=swap">
<style>
:root{
  --blue:#1f8fd0;
  --blue-light:#2aa6dc;
  --blue-deep:#1b6fb3;
  --navy:#0f3b66;
  --navy-dark:#0b2f52;
  --ink:#1d2a36;
  --text:#5a6470;
  --white:#ffffff;
  --gold:#f5b21b;
}
*{margin:0;padding:0;box-sizing:border-box}
html,body{width:1200px;height:4508px;overflow:hidden}
body{position:relative;background:var(--white);font-family:'Roboto',Arial,sans-serif;color:var(--ink)}
.abs{position:absolute}
.heading{font-family:'Oswald',Arial,sans-serif;font-weight:600;text-transform:uppercase}
.btn{position:absolute;display:flex;align-items:center;justify-content:center;border-radius:30px;font-family:'Oswald',Arial,sans-serif;font-weight:500;text-transform:uppercase;color:var(--white);background:linear-gradient(180deg,var(--blue-light),var(--blue-deep))}

/* header */
.topline{left:0;top:0;width:1200px;height:4px;background:var(--navy)}
.brand{display:flex;align-items:center;gap:10px}
.brand-mark{width:52px;height:52px;background:linear-gradient(160deg,var(--blue-light),var(--blue-deep))}
.brand-name{font-family:'Oswald',Arial,sans-serif;font-weight:600;font-size:22px;line-height:1.05;color:var(--blue-deep);letter-spacing:1px}
.header-brand{left:154px;top:52px}
.callus{left:684px;top:32px;font-family:'Oswald',Arial,sans-serif;font-weight:500;font-size:22px;color:var(--blue)}
.quote-btn{left:929px;top:26px;width:119px;height:40px;font-size:13px}
.nav{left:436px;top:91px;display:flex;font-family:'Oswald',Arial,sans-serif;font-weight:600;font-size:14px;color:var(--ink)}
.nav span{position:absolute;white-space:nowrap}
.nav .active{color:var(--blue)}

/* hero */
.hero{left:0;top:145px}
.hero-title{left:250px;top:276px;font-size:52px;line-height:61px;color:var(--white);font-weight:600;letter-spacing:1px}
.hero-btn{left:245px;top:541px;width:135px;height:52px;font-size:17px;border:3px solid var(--white)}

/* services */
.section-title{width:1200px;left:0;text-align:center;color:var(--blue);font-size:58px}
.card{position:absolute;width:285px;height:318px;background:var(--white);border-radius:6px 6px 6px 46px;box-shadow:0 10px 28px rgba(20,40,70,.16);overflow:hidden;text-align:center}
.card-photo{height:175px;background:linear-gradient(135deg,#6f7c88,#2f3a45 55%,#8b99a6)}
.card-title{margin-top:28px;font-family:'Oswald',Arial,sans-serif;font-weight:600;font-size:16px;color:var(--navy);text-transform:uppercase}
.card-text{margin:14px auto 0;width:245px;font-size:12px;line-height:16px;color:var(--text)}

/* about */
.about{left:0;top:1798px;width:1200px;height:549px;background:linear-gradient(180deg,var(--blue-light),var(--blue-deep))}
.about-title{left:150px;top:1890px;font-size:60px;color:var(--white);font-weight:700}
.about-text{left:150px;top:1985px;width:440px;font-size:14px;line-height:22.5px;color:var(--white)}
.about-btn{left:150px;top:2188px;width:146px;height:47px;font-size:17px;background:var(--blue-light);box-shadow:0 4px 10px rgba(0,0,0,.12)}
.about-art{left:700px;top:1871px;width:280px;height:385px;background:linear-gradient(180deg,rgba(255,255,255,.28),rgba(255,255,255,.08))}

/* reviews */
.review{position:absolute;width:290px;text-align:center}
.avatar{width:122px;height:122px;border-radius:50%;margin:0 auto;background:linear-gradient(180deg,#e3e3e3,#b9b9b9)}
.review-text{margin:32px auto 0;width:262px;font-style:italic;font-size:13px;line-height:17px;color:var(--text)}
.review-name{margin-top:14px;font-family:'Oswald',Arial,sans-serif;font-weight:500;font-size:21px;color:var(--blue);text-transform:uppercase}
.stars{margin-top:4px;display:flex;justify-content:center;gap:2px}

/* call to action */
.cta{left:0;top:2947px;width:1200px;height:408px;background:linear-gradient(180deg,#1d7cc0,#1a6cb0);}
.cta-title{left:0;width:1200px;top:3050px;text-align:center;font-size:44px;line-height:63px;color:var(--white);letter-spacing:1px}
.cta-btn{left:504px;top:3194px;width:192px;height:50px;font-size:17px;background:var(--navy);border:2px solid var(--white)}

/* choice */
.choice-title{left:232px;top:3452px;font-size:50px;color:var(--blue);white-space:nowrap}
.feature{position:absolute;width:300px;text-align:center}
.feature svg{display:block;margin:0 auto}
.feature-title{margin-top:28px;font-family:'Oswald',Arial,sans-serif;font-weight:600;font-size:21px;color:var(--ink);text-transform:uppercase}
.feature-text{margin:12px auto 0;width:270px;font-size:13px;line-height:18px;color:var(--text)}
.feature .btn{position:relative;margin:10px auto 0;width:102px;height:27px;font-size:12px}

/* footer */
.footer{left:0;top:3930px}
.footer-brand{left:157px;top:4228px}
.footer-brand .brand-name{color:var(--blue-light)}
.social{left:170px;top:4319px;display:flex;gap:14px}
.social span{width:44px;height:44px;border-radius:50%;border:2px solid var(--white)}
.divider{width:1px;height:210px;top:4215px;background:rgba(255,255,255,.45)}
.foot-col{top:4222px;color:var(--white)}
.foot-col h4{font-family:'Oswald',Arial,sans-serif;font-weight:500;font-size:17px;margin-bottom:14px;text-transform:uppercase}
.foot-col li{list-style:none;font-size:13px;line-height:25px}
.contact-item{display:flex;align-items:center;gap:12px;font-size:13px;line-height:19px;margin-bottom:14px}
.contact-icon{flex:none;width:36px;height:36px;border-radius:50%;background:var(--white);display:flex;align-items:center;justify-content:center}
.copyright{left:0;width:1200px;top:4461px;text-align:center;font-size:11px;color:var(--white);word-spacing:2px}
.copyright span{margin:0 12px}
</style>
</head>
<body>

<!-- header -->
<div class="abs topline"></div>
<div class="abs brand header-brand">
  <div class="brand-mark"></div>
  <div class="brand-name">HARBORLINE<br>AUTO GLASS</div>
</div>
<div class="abs callus">CALL US: 555 014 2290</div>
<div class="btn quote-btn">Get a quote</div>
<div class="abs nav">
  <span class="active" style="left:0">HOME</span>
  <span style="left:89px">ABOUT US</span>
  <span style="left:202px">SERVICES</span>
  <span style="left:313px">WHY US?</span>
  <span style="left:416px">WE'RE HIRING</span>
  <span style="left:554px">CONTACT</span>
</div>

<!-- hero -->
<svg class="abs hero" width="1200" height="721" viewBox="0 0 1200 721">
  <defs>
    <linearGradient id="heroPhoto" x1="0" y1="0" x2="1" y2="1">
      <stop offset="0" stop-color="#4c5866"/>
      <stop offset=".5" stop-color="#2a323c"/>
      <stop offset="1" stop-color="#3f5a78"/>
    </linearGradient>
    <linearGradient id="heroBlue" x1="0" y1="0" x2="1" y2="0">
      <stop offset="0" stop-color="#1b6fb3"/>
      <stop offset="1" stop-color="#2a9bd8"/>
    </linearGradient>
  </defs>
  <polygon points="0,0 1200,0 1200,458 0,721" fill="url(#heroPhoto)" role="img" aria-label="Technicians fitting a windshield with suction cups"/>
  <polygon points="680,578 1200,458 1200,575" fill="url(#heroBlue)"/>
  <polygon points="0,721 1200,575 1200,721" fill="#ffffff"/>
</svg>
<h1 class="abs heading hero-title">Schedual a service<br>within 24 hour with<br>one of our certified<br>technicians.</h1>
<div class="btn hero-btn">Schedule</div>

<!-- services -->
<h2 class="abs heading section-title" style="top:852px">Our Services</h2>
<div class="card" style="left:150px;top:980px">
  <div class="card-photo" role="img" aria-label="Technician repairing a windshield chip"></div>
  <div class="card-title">Windshield Repair</div>
  <p class="card-text">Lorem ipsum dolor sit amet, consectetur aincididunt ut Lorem ipsum dolor sit amet, consectetur aincididunt ut labore</p>
</div>
<div class="card" style="left:457px;top:980px">
  <div class="card-photo" role="img" aria-label="Technician carrying a new windshield"></div>
  <div class="card-title">Windshield Replacment</div>
  <p class="card-text">Lorem ipsum dolor sit amet, consectetur aincididunt ut Lorem ipsum dolor sit amet, consectetur aincididunt ut labore</p>
</div>
<div class="card" style="left:763px;top:980px">
  <div class="card-photo" role="img" aria-label="Technician fitting a rear windshield"></div>
  <div class="card-title">Rear Windshield Replacment</div>
  <p class="card-text">Lorem ipsum dolor sit amet, consectetur aincididunt ut Lorem ipsum dolor sit amet, consectetur aincididunt ut labore</p>
</div>
<div class="card" style="left:150px;top:1349px">
  <div class="card-photo" role="img" aria-label="Cracked side mirror and window"></div>
  <div class="card-title">Side Window Replacment</div>
  <p class="card-text">Lorem ipsum dolor sit amet, consectetur aincididunt ut Lorem ipsum dolor sit amet, consectetur aincididunt ut labore</p>
</div>
<div class="card" style="left:457px;top:1349px">
  <div class="card-photo" role="img" aria-label="Technicians replacing a car window in a workshop"></div>
  <div class="card-title">Car Window Replacment</div>
  <p class="card-text">Lorem ipsum dolor sit amet, consectetur aincididunt ut Lorem ipsum dolor sit amet, consectetur aincididunt ut labore</p>
</div>
<div class="card" style="left:763px;top:1349px">
  <div class="card-photo" role="img" aria-label="Technician repairing a power window"></div>
  <div class="card-title">Power Window Repair.</div>
  <p class="card-text">Lorem ipsum dolor sit amet, consectetur aincididunt ut Lorem ipsum dolor sit amet, consectetur aincididunt ut labore</p>
</div>

<!-- about -->
<div class="abs about"></div>
<h2 class="abs heading about-title">About Us</h2>
<p class="abs about-text">Lorem ipsum dolor sit amet, consectetur adipiscing elit, sed do eiusmod tempor incididunt ut labore et dolore magna aliqua. Ut enim ad minim veniam, quis nostrud exercitation ullamco laboris nisi ut aliquip ex ea commodo consequat. Duis aute irure dolor in reprehenderit in voluptate velit esse cillum dolore eu fugiat nulla pariatur. Excepteur sint occaecat cupidatat non proident, sunt in culpa qui officia deserunt mollit anim id est laborum.</p>
<div class="btn about-btn">Contact Us</div>
<div class="abs about-art" role="img" aria-label="Illustration of a cracked windshield"></div>

<!-- reviews -->
<h2 class="abs heading section-title" style="top:2420px">Customer Reviews</h2>
<div class="review" style="left:145px;top:2577px">
  <div class="avatar" role="img" aria-label="Customer portrait"></div>
  <p class="review-text">"Lorem ipsum dolor sit amet, consect adipiscing elit, sed do eiusmod tempor incididunt utmagna aliqua. Ut enim ad commodo consequat."</p>
  <div class="review-name">- Marcus Dale</div>
  <div class="stars"><svg width="90" height="16" viewBox="0 0 90 16"><g fill="#f5b21b"><path id="st" d="M8 0l2.4 5.2 5.6.6-4.2 3.8 1.2 5.6L8 12.4 3 15.2l1.2-5.6L0 5.8l5.6-.6z"/><use href="#st" x="18"/><use href="#st" x="36"/><use href="#st" x="54"/><use href="#st" x="72"/></g></svg></div>
</div>
<div class="review" style="left:453px;top:2577px">
  <div class="avatar" role="img" aria-label="Customer portrait"></div>
  <p class="review-text">"Lorem ipsum dolor sit amet, consect adipiscing elit, sed do eiusmod tempor incididunt utmagna aliqua. Ut enim ad commodo consequat."</p>
  <div class="review-name">- Owen Tarly</div>
  <div class="stars"><svg width="90" height="16" viewBox="0 0 90 16"><g fill="#f5b21b"><use href="#st"/><use href="#st" x="18"/><use href="#st" x="36"/><use href="#st" x="54"/><use href="#st" x="72"/></g></svg></div>
</div>
<div class="review" style="left:761px;top:2577px">
  <div class="avatar" role="img" aria-label="Customer portrait"></div>
  <p class="review-text">"Lorem ipsum dolor sit amet, consect adipiscing elit, sed do eiusmod tempor incididunt utmagna aliqua. Ut enim ad commodo consequat."</p>
  <div class="review-name">- Leo Brandt</div>
  <div class="stars"><svg width="90" height="16" viewBox="0 0 90 16"><g fill="#f5b21b"><use href="#st"/><use href="#st" x="18"/><use href="#st" x="36"/><use href="#st" x="54"/><use href="#st" x="72"/></g></svg></div>
</div>

<!-- call to action -->
<div class="abs cta" role="img" aria-label="Blue tinted photo of a glass workshop"></div>
<h2 class="abs heading cta-title">Schedual a service within 24 hour with<br>one of our certified technicians.</h2>
<div class="btn cta-btn">Schedule Now</div>

<!-- best choice -->
<h2 class="abs heading choice-title">The Best Choice For Auto Glass Repair</h2>
<div class="feature" style="left:125px;top:3587px">
  <svg width="120" height="120" viewBox="0 0 120 120" fill="none" stroke="#1f8fd0" stroke-width="3">
    <rect x="10" y="8" width="72" height="102"/>
    <path d="M24 30h44M24 44h44M24 58h44M24 72h30M24 86h24"/>
    <path d="M70 92l38-38 8 8-38 38-12 4z"/>
  </svg>
  <div class="feature-title">Stress Free Claim</div>
  <p class="feature-text">Lorem ipsum dolor sit amet, consectetur incididunt ut labore et dolore aliqua.</p>
  <div class="btn">Learn More</div>
</div>
<div class="feature" style="left:450px;top:3587px">
  <svg width="120" height="120" viewBox="0 0 120 120" fill="none" stroke="#1f8fd0" stroke-width="3">
    <path d="M60 8c-17 0-30 13-30 29 0 22 30 50 30 50s30-28 30-50C90 21 77 8 60 8z"/>
    <circle cx="60" cy="36" r="12"/>
    <path d="M30 80H18L6 112h108L102 80H90M20 112l22-24M100 112L78 88"/>
  </svg>
  <div class="feature-title">Shops Near You</div>
  <p class="feature-text">Lorem ipsum dolor sit amet, consectetur incididunt ut labore et dolore aliqua.</p>
  <div class="btn">Find A Shop</div>
</div>
<div class="feature" style="left:774px;top:3587px">
  <svg width="120" height="120" viewBox="0 0 120 120" fill="none" stroke="#1f8fd0" stroke-width="3">
    <path d="M52 6h16l3 13 9 4 11-7 11 11-7 11 4 9 13 3v16l-13 3-4 9 7 11-11 11-11-7-9 4-3 13H52l-3-13-9-4-11 7-11-11 7-11-4-9-13-3V52l13-3 4-9-7-11 11-11 11 7 9-4z"/>
    <circle cx="60" cy="60" r="26"/>
    <path d="M46 74l20-20M62 44a10 10 0 0 1 14 14l-6-2-4 4 2 6a10 10 0 0 1-14-14"/>
  </svg>
  <div class="feature-title">Superipr Repairs</div>
  <p class="feature-text">Lorem ipsum dolor sit amet, consectetur incididunt ut labore et dolore aliqua.</p>
  <div class="btn">Learn More</div>
</div>

<!-- footer -->
<svg class="abs footer" width="1200" height="578" viewBox="0 0 1200 578">
  <defs>
    <linearGradient id="footNavy" x1="0" y1="0" x2="0" y2="1">
      <stop offset="0" stop-color="#0f3b66"/>
      <stop offset="1" stop-color="#0b2f52"/>
    </linearGradient>
  </defs>
  <polygon points="0,136 700,136 0,259" fill="#1f8fd0"/>
  <polygon points="0,259 1200,5 1200,578 0,578" fill="url(#footNavy)"/>
</svg>
<div class="abs brand footer-brand">
  <div class="brand-mark"></div>
  <div class="brand-name">HARBORLINE<br>AUTO GLASS</div>
</div>
<div class="abs social" aria-label="Social media links"><span></span><span></span><span></span></div>
<div class="abs divider" style="left:434px"></div>
<div class="abs divider" style="left:617px"></div>
<div class="abs divider" style="left:848px"></div>
<div class="abs foot-col" style="left:457px">
  <h4>Links</h4>
  <ul><li>Home</li><li>About us</li><li>Services</li><li>Locations</li><li>We're Hiring</li><li>My Appointment</li></ul>
</div>
<div class="abs foot-col" style="left:640px">
  <h4>Services</h4>
  <ul><li>Windshield REPAIR</li><li>Windshield replacment</li><li>Rear Windshield Replacment</li><li>Side Window Replacment</li><li>car window replacment</li><li>Power Window Repair.</li></ul>
</div>
<div class="abs foot-col" style="left:871px">
  <h4>Contact Us</h4>
  <div class="contact-item">
    <span class="contact-icon"><svg width="16" height="20" viewBox="0 0 16 20"><path d="M8 0a8 8 0 0 0-8 8c0 6 8 12 8 12s8-6 8-12a8 8 0 0 0-8-8zm0 11a3 3 0 1 1 0-6 3 3 0 0 1 0 6z" fill="#1f8fd0"/></svg></span>
    <span>123 ipsum dolor sit amet,<br>consectetur adipiscing</span>
  </div>
  <div class="contact-item">
    <span class="contact-icon"><svg width="18" height="14" viewBox="0 0 18 14"><rect width="18" height="14" rx="2" fill="#1f8fd0"/><path d="M1 2l8 6 8-6" stroke="#fff" stroke-width="1.6" fill="none"/></svg></span>
    <span>info@harborline-example.com</span>
  </div>
  <div class="contact-item">
    <span class="contact-icon"><svg width="18" height="18" viewBox="0 0 18 18"><path d="M4 1l3 4-2 2c1 2 3 4 5 5l2-2 4 3-2 4C7 17 1 11 0 3z" fill="#1f8fd0"/></svg></span>
    <span>555 010 4477</span>
  </div>
</div>
<div class="abs copyright"><span>© 2022 HARBORLINE AUTO GLASS</span><span>PRIVACY POLICY</span></div>

</body>
</html>
```